Carrying bags for customer visit

I am looking to make a carrying case that can be used to carry small presents, gifts, our brochure (20 inch X20 inch) and sometimes our samples (which are printed circuit boards that have a size of 24X15). The case should look elegant, show our company logo and our slogan "BOARDS ARE OUR CRAFT". You can try to download our logo from our web site www.lunvaxcraft.net. I want a contemporary and cool feel of the carrying case that can be any materials. I prefer to use recyclable materials that reflects our company's business philosophy of practicing sustanbility. Also I would like to add Chinese name “泰恒工坊(江门)有限公司" in the bag.

Target Market(s)

Corporate customers who will come into contact with our companies

Colors

Designer to choose colors to be used in the design.

Requirements
Must have
• It has to be attractive and people wanting to use them on a regular basis. Therefore, the logo display and our slogan should be subtle. I want the carrying bags not to be very expensive to produce.

```html
<!DOCTYPE html>
<html lang="en">
<head>
<meta charset="utf-8">
<title>Lunvax Carrying Bag – Front Panel</title>
<link rel="stylesheet" href="https://fonts.googleapis.com/css2?family=Montserrat:wght@300;400;700;800&family=Noto+Sans+SC:wght@300;400&display=swap">
<style>
  :root {
    --backdrop: #e4e4e4;
    --panel-white: #f3f3f3;
    --circuit-grey: #7d7d7d;
    --circuit-grey-light: #8a8a8a;
    --brand-green: #0b5a2c;
    --ink: #2b2b2b;
    --label-text: #ffffff;
  }
  * { box-sizing: border-box; margin: 0; padding: 0; }
  html, body {
    width: 1200px; height: 1200px; overflow: hidden;
    background: var(--backdrop);
  }
  .bag-front {
    position: absolute;
    left: 220px; top: 100px;
    width: 760px; height: 1000px;
    background: var(--panel-white);
    overflow: hidden;
    box-shadow: 0 20px 40px rgba(0,0,0,0.12);
  }
  .circuit-field {
    position: absolute; left: 0; width: 100%;
    background: linear-gradient(180deg, var(--circuit-grey-light), var(--circuit-grey));
  }
  .circuit-field--top { top: 0; height: 290px; }
  .circuit-field--bottom { top: 740px; height: 260px; }
  .band-shapes { position: absolute; inset: 0; }
  .brand-block {
    position: absolute; left: 0; right: 0; top: 390px;
    display: flex; flex-direction: column; align-items: center;
  }
  .brand-name {
    font-family: 'Montserrat', sans-serif;
    font-weight: 800;
    font-size: 104px;
    letter-spacing: 6px;
    color: var(--brand-green);
    line-height: 1;
  }
  .slogan-rule {
    width: 460px; height: 2px;
    background: var(--brand-green);
    margin-top: 44px;
  }
  .slogan {
    margin-top: 12px;
    font-family: 'Montserrat', sans-serif;
    font-size: 44px;
    color: var(--ink);
    letter-spacing: -0.5px;
    white-space: nowrap;
  }
  .slogan__light { font-weight: 300; }
  .slogan__bold { font-weight: 700; color: var(--brand-green); }
  .company-label {
    position: absolute; left: 180px; top: 893px;
    width: 400px; height: 50px;
    background: var(--brand-green);
    border-radius: 6px;
    display: flex; align-items: center; justify-content: center;
    font-family: 'Noto Sans SC', sans-serif;
    font-weight: 300;
    font-size: 26px;
    letter-spacing: 2px;
    color: var(--label-text);
  }
</style>
</head>
<body>
  <main class="bag-front">
    <div class="circuit-field circuit-field--top" role="img" aria-label="Grey printed circuit board trace pattern"></div>
    <div class="circuit-field circuit-field--bottom" role="img" aria-label="Grey printed circuit board trace pattern"></div>

    <svg class="band-shapes" viewBox="0 0 760 1000" width="760" height="1000" aria-hidden="true">
      <polygon points="0,262 760,282 760,350 400,338 0,330" fill="var(--panel-white)"/>
      <polygon points="0,280 400,312 760,298 760,325 400,338 0,304" fill="var(--brand-green)"/>
      <polygon points="0,304 400,338 760,325 760,740 0,740" fill="var(--panel-white)"/>
      <polygon points="0,712 400,694 760,712 760,738 400,720 0,738" fill="var(--brand-green)"/>
      <polygon points="0,738 400,720 760,738 760,752 0,752" fill="var(--panel-white)"/>
    </svg>

    <section class="brand-block">
      <div class="brand-name">LUNVAX</div>
      <div class="slogan-rule"></div>
      <p class="slogan"><span class="slogan__light">BOARDS ARE OUR </span><span class="slogan__bold">CRAFT</span></p>
    </section>

    <div class="company-label" lang="zh">泰恒工坊(江门)有限公司</div>
  </main>
</body>
</html>
```